Electrical Contracting business card design

We need a simple business card design for an Electrical Contracting business. A simple design would be appreciated
This company has 2 directors so on one it would have Dale Morrow & another with Shane Morrow.
Updates

Project Deadline Extended
Reason: Hello A few designers have asked for a logo unfortunately we don't have one so have extended deadline to see who can help us out with this. CHEERS

Project Deadline Extended
Reason: Waiting for business partner to return from xmas break. cheers

Industry/Entity Type

Business

Contact Information for Business Card

Quolvin Electrical Services P/L
REC: 63417
Residential Commercial Industrial
Service-Repairs-Renovations-Installations-Telephone-Data
Dale Morrow-Ph: 0437 612 388
Email: dale@quolvinelectrical.com.au

Requirements
Should not have
• The design should not have any electrical appliances in it ie: power-points, leads, houses etc.

```html
<!DOCTYPE html>
<html lang="en">
<head>
<meta charset="utf-8">
<title>Quolvin Electrical Services – Business Card</title>
<link rel="stylesheet" href="https://fonts.googleapis.com/css2?family=Open+Sans:wght@300;400&display=swap">
<style>
  :root {
    --backdrop: #2b1a12;
    --blue-light: #1fa0d2;
    --blue-dark: #0d4f7c;
    --black: #000000;
    --white: #ffffff;
    --bullet: #7fd0f0;
  }
  * { box-sizing: border-box; margin: 0; padding: 0; }
  html, body {
    width: 1200px; height: 1000px; overflow: hidden;
    background: var(--backdrop);
    font-family: "Open Sans", Arial, sans-serif;
    color: var(--white);
  }
  .stage {
    position: relative; width: 1200px; height: 1000px;
  }
  .card {
    position: absolute; left: 220px;
    width: 760px; height: 440px;
    background: var(--black);
    overflow: hidden;
    box-shadow: 0 10px 30px rgba(0,0,0,.55);
  }
  .card--front { top: 40px; }
  .card--back  { top: 520px; }
  .card__band {
    position: absolute; top: 0; left: 0; height: 100%;
    background: linear-gradient(180deg, var(--blue-light) 0%, var(--blue-dark) 100%);
  }
  .card--front .card__band { width: 47%; }
  .card--back .card__band { width: 48%; }

  .brand {
    position: absolute;
    display: flex; align-items: center; gap: 14px;
    font-weight: 400; color: var(--white);
    white-space: nowrap;
  }
  .brand__square { background: var(--white); flex: none; }
  .card--front .brand {
    left: 250px; top: 190px; font-size: 28px;
  }
  .card--front .brand__square { width: 34px; height: 34px; }
  .card--back .brand {
    left: 340px; top: 40px; font-size: 15px;
  }
  .card--back .brand__square { width: 16px; height: 16px; }
  .licence {
    position: absolute; left: 340px; top: 72px;
    font-size: 14px; font-weight: 400; letter-spacing: .3px;
  }

  .services {
    position: absolute; left: 60px;
    list-style: none; font-size: 23px; font-weight: 400; line-height: 31px;
  }
  .services li { position: relative; padding-left: 20px; }
  .services li::before {
    content: ""; position: absolute; left: 0; top: 13px;
    width: 7px; height: 7px; border-radius: 50%; background: var(--bullet);
  }
  .services--sectors { top: 120px; }
  .services--work { top: 250px; }

  .contact {
    position: absolute; right: 40px; bottom: 50px;
    text-align: right; font-weight: 300;
  }
  .contact__name { font-size: 44px; line-height: 52px; }
  .contact__line { font-size: 19px; line-height: 28px; }
</style>
</head>
<body>
<main class="stage">
  <section class="card card--front" aria-label="Card front">
    <div class="card__band"></div>
    <div class="brand">
      <span class="brand__square"></span>
      <span class="brand__name">Quolvin Electrical Services</span>
    </div>
  </section>

  <section class="card card--back" aria-label="Card back">
    <div class="card__band"></div>
    <ul class="services services--sectors">
      <li>Residential</li>
      <li>Commercial</li>
      <li>Industrial</li>
    </ul>
    <ul class="services services--work">
      <li>Service</li>
      <li>Repairs</li>
      <li>Renovations</li>
      <li>Installations</li>
      <li>Telephone</li>
      <li>Data</li>
    </ul>
    <div class="brand">
      <span class="brand__square"></span>
      <span class="brand__name">Quolvin Electrical Services</span>
    </div>
    <p class="licence">P/L REC: 63417</p>
    <div class="contact">
      <p class="contact__name">Dale Morrow</p>
      <p class="contact__line">p: 0437 612 388</p>
      <p class="contact__line">e: dale@quolvinelectrical.com.au</p>
    </div>
  </section>
</main>
</body>
</html>
```